Looking for a cool, modern Cannabis Jar Label

I want you to come up with a better, modern look for a label.

I need it sized to 4” x 3” - I plan to print directly to label printer.

I want you to use Photoshop and deliver me a layered PSD file that I can edit and modify the information as needed..

The label information will need to include places for:
(1) Strain Name - most important part of label - larger font size than rest - example Marlow Frost, KTV #7, Copperleaf Haze
(2) Pricing - for Gram, 1/8, 1/4, 1/2. and Ounce
(3) Strain Designation (Hybrid, Indica or Sativa) - maybe color coded, different color for Indica v. Sativa, just an idea
(4) THC and CBD percentages - for example 23% THC and 0.05% CBD
(5) Farm name - a place where we can add the name/logo of the business that produced the product. example - Bramwell Farms

I have attached a simple mockup showing the information.

I have also attached a few samples of labels we like to give you an idea of the look and feel we are going for.

I am wanting a very clean, modern, classy, readable look.The font will use is Gotham Font.

HI Everyone! Thank you for all of your designs. I am requesting an extension because I need more time to give adequate feedback to the designers. Thank you for your participation and all of your efforts! I will be making a decision soon!

• Gotham Font

Designer to choose colors to be used in the design.

• Thank you for your designs. I am sorry i have been slow in providing feedback, things have been really busy around here!
• I wanted to give some group general feedback. After reviewing all of the designs, there is a common theme among all of the designs that I would like to see changed.
• I would like to see the per gram pricing more prominent on the label. This is what most people are looking for when they are purchasing the product. So I would like to see this stand out from the other pricing tiers. As I think about it, they don't all need to be grouped together in a line. You could have the Per Gram pricing front and center some where and then the other pricing tiers grouped together somewhere else on the label.
• This is the order of importance of items on the label. Items at the the top of the list should be bigger than those below it.
• 1. Strain name
• 2. Pricing - being per gram the most important of all prices
• 3. THC/CBD percentages
• 4. Strain Type (indica, sativa, hybrid)
• 5. Farm name/logo
• When laying out these labels, they will be going on rounded jars and they will be on display. Think of jars with fancy labels in a candy store. They need to be eye catchy, appealing, but easy read.
• Thank you for all of your hard work, everyone is doing a great job.
• Best,
• Nadia

```html
<!DOCTYPE html>
<html lang="en">
<head>
<meta charset="utf-8">
<title>Strain Jar Label</title>
<link rel="stylesheet" href="https://fonts.googleapis.com/css2?family=Montserrat:wght@400;500&display=swap">
<style>
  :root {
    --forest: #2f4113;
    --leaf: #7b9b4c;
    --leaf-soft: #a9c07a;
    --cream: #eaf6bd;
    --paper: #ffffff;
  }
  * { margin: 0; padding: 0; box-sizing: border-box; }
  html, body { width: 1200px; height: 900px; overflow: hidden; background: var(--paper); }
  body { font-family: "Montserrat", sans-serif; color: var(--forest); }
  .label { position: relative; width: 1200px; height: 900px; }
  .label-border {
    position: absolute; left: 16px; top: 16px; width: 1168px; height: 866px;
    border: 3px dotted var(--forest);
  }
  .leaf-art {
    position: absolute; left: 430px; top: 35px; width: 330px; height: 310px;
    background: radial-gradient(ellipse at 50% 60%, #9ab56a 0%, #b9cf8e 45%, rgba(255,255,255,0) 72%);
  }
  .strain-name {
    position: absolute; left: 0; top: 352px; width: 1180px; text-align: center;
    font-size: 78px; font-weight: 500; letter-spacing: 0.02em; line-height: 1;
  }
  .rule-thick { position: absolute; left: 66px; top: 456px; width: 1050px; height: 3px; background: var(--forest); }
  .rule-thin { position: absolute; left: 106px; top: 466px; width: 974px; height: 1px; background: var(--forest); }
  .type-band {
    position: absolute; left: 66px; top: 504px; width: 740px; height: 54px; background: var(--forest);
  }
  .type-band span {
    position: absolute; left: 191px; top: 6px; color: var(--cream);
    font-size: 40px; font-weight: 400; letter-spacing: 0.62em; line-height: 1;
  }
  .divider { position: absolute; left: 803px; top: 504px; width: 3px; height: 268px; background: var(--forest); }
  .farm-name {
    position: absolute; left: 815px; top: 532px; width: 250px; text-align: center;
    font-size: 50px; font-weight: 400; line-height: 68px;
  }
  .farm-name .logo-word { color: var(--leaf); }
  .grown-band {
    position: absolute; left: 805px; top: 770px; width: 308px; height: 54px; background: var(--forest);
    color: var(--paper); font-size: 30px; letter-spacing: 0.1em; text-align: center; line-height: 56px;
  }
  .price {
    position: absolute; top: 650px; width: 110px; height: 90px; text-align: center;
  }
  .price svg { position: absolute; left: 0; top: 30px; }
  .price-amount { position: relative; font-size: 26px; font-weight: 500; line-height: 1; }
  .price-unit { position: relative; margin-top: 5px; font-size: 24px; color: var(--leaf); line-height: 1; }
  .potency {
    position: absolute; top: 780px; font-size: 46px; font-weight: 400; line-height: 1; white-space: nowrap;
  }
  .potency .dots { font-size: 28px; color: var(--leaf); letter-spacing: 0.02em; margin-left: 4px; }
  .potency .compound { font-size: 28px; letter-spacing: 0.04em; }
</style>
</head>
<body>
<main class="label">
  <div class="label-border"></div>
  <div class="leaf-art" role="img" aria-label="Green cannabis leaf illustration"></div>
  <h1 class="strain-name">STRAIN NAME</h1>
  <div class="rule-thick"></div>
  <div class="rule-thin"></div>

  <div class="type-band"><span>INDICA</span></div>
  <div class="divider"></div>

  <div class="farm-name">Bramwell<br>Farms<br><span class="logo-word">Logo</span></div>
  <div class="grown-band">GROWN BY</div>

  <div class="price" style="left:58px">
    <svg width="110" height="60" viewBox="0 0 110 60"><path d="M8 6 A47 47 0 0 0 102 6" fill="none" stroke="var(--leaf)" stroke-width="6"/></svg>
    <div class="price-amount">10$</div><div class="price-unit">g</div>
  </div>
  <div class="price" style="left:218px">
    <svg width="110" height="60" viewBox="0 0 110 60"><path d="M8 6 A47 47 0 0 0 102 6" fill="none" stroke="var(--leaf)" stroke-width="6"/></svg>
    <div class="price-amount">35$</div><div class="price-unit">1/8</div>
  </div>
  <div class="price" style="left:380px">
    <svg width="110" height="60" viewBox="0 0 110 60"><path d="M8 6 A47 47 0 0 0 102 6" fill="none" stroke="var(--leaf)" stroke-width="6"/></svg>
    <div class="price-amount">70$</div><div class="price-unit">1/4</div>
  </div>
  <div class="price" style="left:533px">
    <svg width="110" height="60" viewBox="0 0 110 60"><path d="M8 6 A47 47 0 0 0 102 6" fill="none" stroke="var(--leaf)" stroke-width="6"/></svg>
    <div class="price-amount">140$</div><div class="price-unit">1/2</div>
  </div>
  <div class="price" style="left:685px">
    <svg width="110" height="60" viewBox="0 0 110 60"><path d="M8 6 A47 47 0 0 0 102 6" fill="none" stroke="var(--leaf)" stroke-width="6"/></svg>
    <div class="price-amount">280$</div><div class="price-unit">oz.</div>
  </div>

  <div class="potency" style="left:64px">23.00%<span class="dots">.......</span> <span class="compound">THC</span></div>
  <div class="potency" style="left:484px">0.05%<span class="dots">.......</span><span class="compound">CBD</span></div>
</main>
</body>
</html>
```